Appealing productlabel for jar with toffees

I run a small import company within confectionary (candy, chocolate, toffees and so on). We are planning launching a series of bulk product - and would like to start up with this article enclosed.<br/>Packaging: Transparent plastic Jar with black lid. Height 22 cm, diameter 15 cm.<br/>I was thinking about a label with the dimensions 10,5 x 14,8 cm. since a have a label sheet in this format (I will probably end up getting it printed at a professional printing company)<br/>Unique Selling Points: Great Toffees with great taste. The toffees do NOT stick to your teeth, 1000 gram, hygienically wrapped.<br/>Brand Name ROVA<br/><br/>Buyers/ Clients: Office Supplies

Target Market(s)

Adult professional purchasers within the segmment: Office Supply, Food Service

Font styles to use
Serif

Requirements
Must have
• Appealing, catchy, attractive design
Nice to have
• Surprise me :-)
Should not have
• A traditional candy design which is appealing to kids - the clients will be grown-ups

```html
<!DOCTYPE html>
<html lang="da">
<head>
<meta charset="utf-8">
<title>Karameller med havsalt – label</title>
<link rel="stylesheet" href="https://fonts.googleapis.com/css2?family=Kaushan+Script&family=Oswald:wght@300;500;600;700&display=swap">
<style>
  :root {
    --page-bg: #ffffff;
    --maroon-deep: #4a0c22;
    --maroon: #6f1533;
    --berry: #a41f52;
    --berry-light: #c63a6e;
    --cream: #fde3c4;
    --cocoa: #3a1a12;
    --crimson-edge: #c8124f;
    --white: #ffffff;
  }
  html, body {
    margin: 0;
    padding: 0;
    width: 1200px;
    height: 1000px;
    overflow: hidden;
    background: var(--page-bg);
  }
  .label {
    position: absolute;
    left: 100px;
    top: 145px;
    width: 1000px;
    height: 709px;
    overflow: hidden;
    font-family: "Oswald", "Arial Narrow", sans-serif;
  }
  .label-backdrop {
    position: absolute;
    inset: 0;
    background: radial-gradient(ellipse at 50% 52%, var(--berry-light) 0%, var(--berry) 22%, var(--maroon) 55%, var(--maroon-deep) 100%);
  }
  .brand-name {
    position: absolute;
    top: 52px;
    left: 0;
    width: 100%;
    text-align: center;
    margin: 0;
    font-weight: 700;
    font-size: 58px;
    line-height: 1;
    color: var(--white);
    letter-spacing: 1px;
  }
  .claim-tag {
    position: absolute;
    left: 368px;
    top: 186px;
    padding: 6px 12px 7px;
    background: var(--cream);
    color: var(--cocoa);
    font-weight: 600;
    font-size: 23px;
    line-height: 1.15;
    transform: rotate(-5deg);
    transform-origin: left center;
    border-radius: 2px;
  }
  .claim-tag-tail {
    position: absolute;
    left: 382px;
    top: 232px;
    width: 34px;
    height: 12px;
    transform: rotate(-5deg);
  }
  .product-title {
    position: absolute;
    left: 50px;
    top: 200px;
    width: 900px;
    margin: 0;
    text-align: center;
    font-family: "Kaushan Script", cursive;
    font-weight: 400;
    font-size: 188px;
    line-height: 1.15;
    color: var(--white);
    -webkit-text-stroke: 4px var(--crimson-edge);
    paint-order: stroke fill;
    text-shadow: -8px 10px 0 var(--cocoa), -6px 8px 0 var(--cocoa);
    transform: rotate(-6deg);
  }
  .product-subtitle {
    position: absolute;
    left: 510px;
    top: 408px;
    margin: 0;
    font-family: "Kaushan Script", cursive;
    font-size: 76px;
    line-height: 1;
    color: var(--white);
    transform: rotate(-6deg);
    transform-origin: left center;
  }
  .selling-lines {
    position: absolute;
    left: 0;
    top: 538px;
    width: 100%;
    margin: 0;
    text-align: center;
    font-weight: 600;
    font-size: 42px;
    line-height: 48px;
    color: var(--cream);
  }
  .net-weight {
    position: absolute;
    left: 0;
    top: 660px;
    width: 100%;
    margin: 0;
    text-align: center;
    font-weight: 300;
    font-size: 25px;
    line-height: 1;
    color: var(--white);
  }
</style>
</head>
<body>
  <section class="label">
    <div class="label-backdrop" role="img" aria-label="Maroon and berry sunburst swirl background with a faint small leaf pattern"></div>

    <h2 class="brand-name">MOLLE CANDY</h2>

    <svg class="claim-tag-tail" viewBox="0 0 34 12" aria-hidden="true">
      <polygon points="0,0 34,0 22,6 34,12 0,12" fill="var(--cream)"/>
    </svg>
    <div class="claim-tag">Ikke klistrer i tænderne</div>

    <h1 class="product-title">Karameller</h1>
    <p class="product-subtitle">med havsalt</p>

    <p class="selling-lines">Cool karameller<br>Pjattet gode og Imponerende</p>
    <p class="net-weight">NET WT 1 KG</p>
  </section>
</body>
</html>
```